Business Card *

A business card design
Use the logo uploaded in the brief page.
You may use placeholders in your design layouts.
I will provide the actual business card details to the winning designer.

Logo
Place for contact info (name, title, phone, email, etc)

Requirements
Must have
• Logo

```html
<!DOCTYPE html>
<html lang="en">
<head>
<meta charset="utf-8">
<title>Harrowfield Business Card</title>
<link href="https://fonts.googleapis.com/css2?family=Work+Sans:wght@400;500&display=swap" rel="stylesheet">
<style>
  :root {
    --backdrop: #1b1b1b;
    --card: #2a2a2a;
    --card-edge: #242424;
    --accent: #3fbf4a;
    --mark-grey: #9a9a9a;
    --ink: #f2f2f2;
  }
  * { margin: 0; padding: 0; box-sizing: border-box; }
  html, body {
    width: 1200px; height: 900px; overflow: hidden;
    background: var(--backdrop);
    font-family: "Work Sans", sans-serif;
  }
  .stage {
    position: relative; width: 1200px; height: 900px;
  }
  .card {
    position: absolute; left: 250px; width: 700px; height: 400px;
    background: linear-gradient(135deg, var(--card-edge), var(--card));
    border-bottom: 8px solid var(--accent);
    box-shadow: 0 12px 30px rgba(0,0,0,.55);
  }
  .card--front { top: 30px; }
  .card--back { top: 470px; }

  .brand {
    display: flex; align-items: center; gap: 16px;
  }
  .brand__dot {
    width: 34px; height: 34px; border-radius: 50%;
    background: var(--accent);
  }
  .brand__name {
    font-weight: 500; font-size: 44px; letter-spacing: 1px;
    color: var(--mark-grey); text-transform: uppercase;
  }
  .card--front .brand {
    position: absolute; left: 50%; top: 50%;
    transform: translate(-50%, -50%);
  }
  .card--back .brand {
    position: absolute; left: 50px; top: 50%;
    transform: translateY(-50%);
  }
  .card--back .brand__name { font-size: 36px; }
  .card--back .brand__dot { width: 28px; height: 28px; }

  .divider {
    position: absolute; left: 370px; top: 70px;
    width: 2px; height: 240px; background: var(--accent);
  }
  .contact {
    position: absolute; left: 405px; top: 75px; color: var(--ink);
  }
  .contact__name {
    font-weight: 500; font-size: 30px; color: var(--accent);
    text-transform: uppercase; letter-spacing: .5px;
  }
  .contact__role { font-size: 19px; margin-bottom: 18px; }
  .contact__address { font-size: 19px; line-height: 1.35; margin-bottom: 10px; }
  .contact__line {
    display: flex; align-items: center; gap: 10px;
    font-size: 19px; line-height: 1.5;
  }
  .contact__icon { width: 14px; height: 14px; flex: none; }
</style>
</head>
<body>
<div class="stage">
  <section class="card card--front">
    <div class="brand">
      <span class="brand__dot"></span>
      <span class="brand__name">Harrowfield</span>
    </div>
  </section>

  <section class="card card--back">
    <div class="brand">
      <span class="brand__dot"></span>
      <span class="brand__name">Harrowfield</span>
    </div>
    <div class="divider"></div>
    <div class="contact">
      <p class="contact__name">Daniel Reyes</p>
      <p class="contact__role">Director</p>
      <p class="contact__address">1420 Orchard Lane<br>Springdale, OH 45246</p>
      <p class="contact__line">
        <svg class="contact__icon" viewBox="0 0 16 16"><path d="M4 1l3 3-2 2c1 2 3 4 5 5l2-2 3 3-2 2C7 14 2 9 2 3z" fill="none" stroke="#3fbf4a" stroke-width="1.5"/></svg>
        055 210 48 37
      </p>
      <p class="contact__line">
        <svg class="contact__icon" viewBox="0 0 16 16"><rect x="1" y="3" width="14" height="10" fill="none" stroke="#3fbf4a" stroke-width="1.5"/><path d="M1 3l7 6 7-6" fill="none" stroke="#3fbf4a" stroke-width="1.5"/></svg>
        hello@harrowfield.com
      </p>
      <p class="contact__line">
        <svg class="contact__icon" viewBox="0 0 16 16"><circle cx="8" cy="8" r="6.5" fill="none" stroke="#3fbf4a" stroke-width="1.5"/><path d="M1.5 8h13M8 1.5c-3 3-3 10 0 13M8 1.5c3 3 3 10 0 13" fill="none" stroke="#3fbf4a" stroke-width="1.2"/></svg>
        www.harrowfield.com
      </p>
    </div>
  </section>
</div>
</body>
</html>
```